Consultative Employee Benifits Firm Needs Business Card Design Project

We need a business card design for a new company based in Northern Virginia called "Telman Financial Services, LLC. We are both a wealth management advisory firm, as well as an employee benefits firm, which strives to provide superior creativity in employee benefits plan design and greater client and employee satisfaction. We are obsessed with service and follow up.

Our firm specializes in the areas of group health, life, dental, disability, voluntary benefits, Executive Benefits, HRA and HSA programs. We offer competitive employee benefit packages and pricing models for single or multi-state/multi location companies by maintaining preferred relationships with a large number of regional and national carriers.

Our firm also considers the many dimensions of your wealth through an integrated process we call wealth structuring — a comprehensive, dynamic approach to building, preserving, enjoying and transferring your wealth. And because we are often dealing with complex ownership structures and complicated, changing family dynamics, we bring the highest level of experience and creativity to managing your wealth. We work hard to help ensure that your legacy lasts by preparing your children for the financial challenges and opportunities that are headed their way.

Our final design should communicate an integrated approach to finanial safety and optimization
Updates

 Due to a few designers not accepting due to low budget, I have increased budget payout 19%. 

Project Deadline Extended
Reason: I have only heard from 12 designers. So, maybe I did not give the right amount of time to do the project. For the designers that have submitted their designs, thank you. I have seen three or four designs that I liked and might end up with one of them after it's all over, but I thought I would see between 20 - 25 before everything was over. Dan

Target Market(s)

Professionals; doctors, contractors, small to mid size business owners, ages 50 -65 with nert worth of 2MM

Industry/Entity Type

Financial

Requirements
Must have
• Telman Financial Services, LLC

Dan Telman
President
41957 Marwick Hollow Street
Quenford Glen, 20871

Office: 703 555-0184
Cell: 703 555-0127
Fax: 703 555-0163
Email: dantelman@quorvex.net
Should not have
• No pink or yellow colors.
No generic clipart (coins, dollar signs, money bags, graphs)

```html
<!DOCTYPE html>
<html lang="en">
<head>
<meta charset="utf-8">
<title>Telman Financial Services, LLC – Business Card</title>
<link rel="stylesheet" href="https://fonts.googleapis.com/css2?family=Saira:wght@500;700&display=swap">
<style>
  :root {
    --backdrop: #5b5b5b;
    --card: #000000;
    --brand-blue: #1f86d6;
    --label-blue: #1e6fc0;
    --text-grey: #c9c9c9;
  }
  * { margin: 0; padding: 0; box-sizing: border-box; }
  html, body {
    width: 1200px;
    height: 534px;
    overflow: hidden;
    background: var(--backdrop);
  }
  .canvas {
    position: relative;
    width: 1200px;
    height: 534px;
    font-family: "Saira", "Arial Narrow", sans-serif;
    text-transform: uppercase;
  }
  .card {
    position: absolute;
    top: 119px;
    width: 517px;
    height: 294px;
    background: var(--card);
  }
  .card--front { left: 62px; }
  .card--back { left: 622px; }

  .wordmark {
    color: var(--brand-blue);
    font-weight: 700;
    line-height: 1;
  }
  .card--front .wordmark {
    position: absolute;
    left: 56px;
    top: 106px;
  }
  .card--front .wordmark__name {
    display: block;
    font-size: 62px;
    letter-spacing: 1px;
  }
  .card--front .wordmark__sub {
    display: block;
    font-size: 20px;
    letter-spacing: 0.6px;
    margin-top: 2px;
  }
  .card--back .wordmark {
    position: absolute;
    right: 41px;
    top: 28px;
    text-align: right;
  }
  .card--back .wordmark__name {
    display: block;
    font-size: 40px;
    letter-spacing: 0.5px;
  }
  .card--back .wordmark__sub {
    display: block;
    font-size: 13px;
    letter-spacing: 0.4px;
    margin-top: 1px;
  }

  .contact {
    position: absolute;
    right: 41px;
    top: 117px;
    text-align: right;
    font-weight: 500;
    font-size: 13px;
    line-height: 15.5px;
    letter-spacing: 0.8px;
    color: var(--text-grey);
  }
  .contact__name {
    color: var(--brand-blue);
    font-size: 15px;
    font-weight: 700;
    letter-spacing: 1px;
  }
  .contact__address { margin-top: 14px; }
  .contact__lines { margin-top: 14px; list-style: none; }
  .contact__label { color: var(--label-blue); }
</style>
</head>
<body>
  <main class="canvas">
    <section class="card card--front" aria-label="Card front">
      <div class="wordmark">
        <span class="wordmark__name">Telman</span>
        <span class="wordmark__sub">Financial Services, LLC</span>
      </div>
    </section>

    <section class="card card--back" aria-label="Card back">
      <div class="wordmark">
        <span class="wordmark__name">Telman</span>
        <span class="wordmark__sub">Financial Services, LLC</span>
      </div>
      <div class="contact">
        <p class="contact__name">Dan Telman</p>
        <p class="contact__title">President</p>
        <p class="contact__address">41957 Marwick Hollow Street<br>Quenford Glen, 20871</p>
        <ul class="contact__lines">
          <li><span class="contact__label">O:</span> 703 555-0184</li>
          <li><span class="contact__label">C:</span> 703 555-0127</li>
          <li><span class="contact__label">F:</span> 703 555-0163</li>
          <li><span class="contact__label">E:</span> dantelman@quorvex.net</li>
        </ul>
      </div>
    </section>
  </main>
</body>
</html>
```